Fun and Flexible Word Template Design for Classroom Learning Resources

We're a global arts and education nonprofit based in New York. We're looking for a 2-page Word template design for our new collection of Learning Resources.
Page 1 of the template should include:
1. Lanternfold 7 logo (attached)
2. Resource title
3. Author photo
4. Author bio
5. Resource text
6. Sub-title text
7. Colored call-out box
Page 2 of the template should include:
2. Resource Title (in a smaller font)
3. Resource text
4. Sub-title text
5. Colored call-out box
The design must also adhere to our current brand guidelines: https://stylevault.example/lanternfold-7
We've attached a very basic mock-up that includes the elements listed above. However, we encourage you to be more playful and/or creative with your design.
Our goal is to create a template that is flexible enough to accomodate a variety of resources (samples of 3 different resources are attached), that is also visually appealing enough to attract and hold the attention of busy educators.
Target Market(s)
Educators - Middle School, High School & College
Look and feel

```html
<!DOCTYPE html>
<html lang="en">
<head>
<meta charset="utf-8">
<title>Lanternfold 7 — Learning Resource Template</title>
<link href="https://fonts.googleapis.com/css2?family=Source+Serif+4:opsz,wght@8..60,500;8..60,600&family=Public+Sans:ital,wght@0,400;0,500;1,400&display=swap" rel="stylesheet">
<style>
  :root {
    --backdrop: #898a89;
    --paper: #ffffff;
    --brand-purple: #663399;
    --callout-fill: #e3d2f3;
    --callout-line: #6a35a0;
    --ink: #3b3b3b;
    --ink-dark: #2e2e2e;
    --photo-light: #c9c9c9;
    --photo-dark: #3a3a3a;
  }
  * { box-sizing: border-box; margin: 0; padding: 0; }
  html, body {
    width: 1200px; height: 960px; overflow: hidden;
    background: var(--backdrop);
  }
  body { position: relative; font-family: "Public Sans", Arial, sans-serif; color: var(--ink); }

  .page {
    position: absolute;
    width: 518px; height: 670px;
    background: var(--paper);
    overflow: hidden;
  }
  .page--first { left: 68px; top: 89px; }
  .page--second { left: 613px; top: 200px; }

  /* Brand lockup */
  .brand { position: absolute; display: flex; align-items: center; gap: 8px; }
  .brand__mark { border-radius: 50%; flex: none; }
  .brand__name { font-family: "Public Sans", Arial, sans-serif; font-weight: 500; letter-spacing: 0.08em; text-transform: uppercase; }
  .page--first .brand { left: 326px; top: 21px; }
  .page--first .brand__mark { width: 38px; height: 38px; background: var(--paper); }
  .page--first .brand__name { color: var(--paper); font-size: 14.5px; }
  .page--second .brand { left: 361px; top: 21px; }
  .page--second .brand__mark { width: 30px; height: 30px; background: var(--brand-purple); }
  .page--second .brand__name { color: var(--brand-purple); font-size: 12px; }

  .header-band { position: absolute; left: 0; top: 0; width: 100%; height: 96px; background: var(--brand-purple); }

  .author-photo {
    position: absolute; left: 31px; top: 25px;
    width: 141px; height: 141px; border-radius: 50%;
    background: radial-gradient(circle at 45% 35%, var(--photo-light), #8d8d8d 55%, var(--photo-dark));
  }

  .author-bio {
    position: absolute; left: 31px; top: 178px; width: 125px;
    font-size: 7.5px; line-height: 11.4px; font-style: italic; text-align: justify;
    color: var(--ink);
  }
  .author-bio .author-name { font-style: italic; letter-spacing: 0.06em; }

  .resource-title {
    position: absolute; left: 191px; top: 119px;
    font-family: "Source Serif 4", Georgia, serif; font-weight: 600;
    font-size: 31px; color: var(--brand-purple); letter-spacing: -0.01em;
  }

  .resource-body p { font-size: 9.3px; line-height: 13.4px; margin-bottom: 6.4px; }
  .page--first .resource-body { position: absolute; left: 192px; top: 178px; width: 295px; }

  .section-title {
    font-family: "Source Serif 4", Georgia, serif; font-weight: 600;
    font-size: 13px; color: var(--ink-dark);
    margin: 13px 0 9px;
  }

  .page--second .resource-body { position: absolute; left: 36px; top: 72px; width: 442px; }
  .continued-title {
    font-family: "Source Serif 4", Georgia, serif; font-weight: 600;
    font-size: 16px; color: var(--brand-purple); margin-bottom: 8px;
  }
  .page--second .section-title { margin: 15px 0 7px; }

  .callout {
    position: absolute; left: 35px; width: 448px; height: 91px;
    background: var(--callout-fill); border: 2px solid var(--callout-line);
    padding: 14px 14px; font-size: 9.6px; line-height: 13px; color: var(--ink);
  }
  .page--first .callout { top: 544px; }
  .page--second .callout { top: 545px; }
</style>
</head>
<body>

<section class="page page--first">
  <div class="header-band"></div>
  <div class="brand">
    <span class="brand__mark"></span>
    <span class="brand__name">Lanternfold 7</span>
  </div>
  <div class="author-photo" role="img" aria-label="Black and white portrait of the resource author"></div>
  <h1 class="resource-title">Lorem ipsum dolor</h1>

  <p class="author-bio"><span class="author-name">AUTHOR NAME</span> dolor sit amet, consectetur adipiscing elit. Morbi ut libero mattis, pellentesque urna eu, iaculis lorem. Interdum et malesuada fames ac ante ipsum primis in faucibus. Duis pellen- tesque orci consectetur sapien vulputate imperdiet. Aliquam erat volutpat. Integer tristique erat lorem, sed posuere enim rhoncus sed. Fusce ut venenatis nulla, sed elementum arcu. Maecenas eu- ismod mauris euismod augue posuere venenatis.</p>

  <div class="resource-body">
    <p>Lorem ipsum dolor sit amet, consectetur adipiscing elit. Morbi ut libero mattis, pellentesque urna eu, iaculis lorem. Interdum et malesuada fames ac ante ipsum primis in faucibus. Duis pellen- tesque orci consectetur sapien vulputate imperdiet. Aliquam erat volutpat. Integer tristique erat lorem, sed posuere enim rhoncus sed. Fusce ut venenatis nulla, sed elementum arcu. Maecenas eu- ismod mauris euismod augue posuere venenatis. Duis id porta ante integer.</p>
    <h2 class="section-title">Lorem ipsum dolor sit</h2>
    <p>Lorem ipsum dolor sit amet, consectetur adipiscing elit. Morbi ut libero mattis, pellentesque urna eu, iaculis lorem. Interdum et malesuada fames ac ante ipsum primis in faucibus. Duis pellen- tesque orci consectetur sapien vulputate imperdiet. Aliquam erat volutpat. Integer tristique erat lorem, sed posuere enim rhoncus sed. Fusce ut venenatis nulla.</p>
    <p>Lorem ipsum dolor sit amet, consectetur adipiscing elit. Morbi ut libero mattis, pellentesque que urna eu, iaculis lorem. Interdum et malesuada fames ac ante ipsum primis iurna eu, iaculis lorem. Interdum et malesuada fames ac ante ipsum primis in faucibus. Duis pellen- tesque orci consectetur sapien vulputate imperdiet.</p>
    <p>Lorem ipsum dolor sit amet, consectetur adipiscing elit. Morbi ut libero mattis, pellentesque urna eu, iaculis lorem. Interdum et malesuada fames ac ante ipsum primis in faucibus. Duis pellen- tesque orci consectetur sapien vulputate imperdiet. Aliquam erat volutpat.</p>
  </div>

  <aside class="callout">Lorem ipsum dolor sit amet, consectetur adipiscing elit. Morbi ut libero mattis, pellentesque urna eu, iaculis lorem. Interdum et malesuada fames ac ante ipsum primis in faucibus. Duis pellen- tesque orci consectetur sapien vulputate imperdiet. Aliquam erat volutpat. Integer tristique erat lorem, sed posuere enim rhoncus sed. Fusce ut venenatis nulla, sed elementum arcu. Maecenas eu- ismod mauris euismod augue posuere venenatis.</aside>
</section>

<section class="page page--second">
  <div class="brand">
    <span class="brand__mark"></span>
    <span class="brand__name">Lanternfold 7</span>
  </div>

  <div class="resource-body">
    <h2 class="continued-title">Lorem ipsum dolor sit (cont'd)</h2>
    <p>Lorem ipsum dolor sit amet, consectetur adipiscing elit. Morbi ut libero mattis, pellentesque urna eu, iaculis lorem. Interdum et malesuada fames ac ante ipsum primis in faucibus. Duis pellen- tesque orci consectetur sapien vulputate imperdiet. Aliquam erat volutpat. Integer tristique erat lorem, sed posuere enim rhoncus sed. Fusce ut venenatis nulla, sed elementum arcu. Maecenas eu- ismod mauris euismod augue posuere venenatis. Duis id porta ante integer.</p>
    <p>Lorem ipsum dolor sit amet, consectetur adipiscing elit. Morbi ut libero mattis, pellentesque urna eu, iaculis lorem. Interdum et malesuada fames ac ante ipsum primis in faucibus. Duis pellen- tesque orci consectetur sapien vulputate imperdiet. Aliquam erat volutpat. Integer tristique erat lorem, sed posuere enim rhoncus sed. Fusce ut venenatis nulla, sed elementum arcu. Maecenas eu- ismod mauris euismod augue posuere venenatis. Duis id porta ante integer.</p>
    <p>Lorem ipsum dolor sit amet, consectetur adipiscing elit. Morbi ut libero mattis, pellentesque urna eu, iaculis lorem. Interdum et malesuada fames ac ante ipsum primis in faucibus. Duis pellen- tesque orci consectetur sapien vulputate imperdiet. Aliquam erat volutpat.r.</p>
    <p>Lorem ipsum dolor sit amet, consectetur adipiscing elit. Morbi ut libero mattis, pellentesque urna eu, iaculis lorem. Interdum et malesuada fames ac ante ipsum primis in faucibus. Duis pellen- tesque orci consectetur sapien vulputate imperdiet.</p>
    <h2 class="section-title">Lorem ipsum dolor sit (cont'd)</h2>
    <p>Lorem ipsum dolor sit amet, consectetur adipiscing elit. Morbi ut libero mattis, pellentesque urna eu, iaculis lorem. Interdum et malesuada fames ac ante ipsum primis in faucibus. Duis pellen- tesque orci consectetur sapien vulputate imperdiet. Aliquam erat volutpat. Integer tristique erat lorem, sed posuere enim rhoncus sed. Fusce ut venenatis nulla.</p>
    <p>Lorem ipsum dolor sit amet, consectetur adipiscing elit. Morbi ut libero mattis, pellentesque urna eu, iaculis lorem. Interdum et malesuada fames ac ante ipsum primis in faucibus. Duis pellen- tesque orci consectetur sapien vulputate imperdiet. Aliquam erat volutpat. Integer tristique erat lorem, sed posuere enim rhoncus sed. Fusce ut venenatis nulla. Aliquam erat volutpat. Integer tristique erat lorem, sed posuere enim rhoncus sed. Fusce ut venenatis nulla, sed elementum arcu. Maecenas eu- ismod mauris euismod augue posuere venenatis. Duis id porta ante integer.</p>
  </div>

  <aside class="callout">Lorem ipsum dolor sit amet, consectetur adipiscing elit. Morbi ut libero mattis, pellentesque urna eu, iaculis lorem. Interdum et malesuada fames ac ante ipsum primis in faucibus. Duis pellen- tesque orci consectetur sapien vulputate imperdiet. Aliquam erat volutpat. Integer tristique erat lorem, sed posuere enim rhoncus sed. Fusce ut venenatis nulla, sed elementum arcu. Maecenas eu- ismod mauris euismod augue posuere venenatis.</aside>
</section>

</body>
</html>
```